Candle Box & Belly Band Design

Design Candle Box for Soy Candles along with a belly band design that can be used on off the shelf coloured boxes. It is for a premium brand of candle - so i want the packaging to reflect this. I have included must haves below.

The candle boxes will be a few different sizes, but for the purpose of the design it would be something like a cube 12 x 12 x 12 cms

The belly band for standard boxes to be something like 5cm wide on a 12 x 12 x 12cms cube box that goes all the way around the top to the bottom - holding the lid on and providing all the relevant information. Example of box with belly band uploaded

Our company Name : Hazel & Pip - our logo is uploaded

Target Market(s)

Premium Candle Buyers

Colors

Designer to choose colors to be used in the design.

Requirements
Must have
• Must have our logo - our logo can be in any colour
• Must state:
• Soy Candle, Hand Poured, Made in Melbourne,
• A space for the fragrance, size and burn time.
• For this project use Lime, Coconut & Elderfllower, 300grams, 50 Hour burn Time

```html
<!DOCTYPE html>
<html lang="en">
<head>
<meta charset="utf-8">
<title>Hazel &amp; Pip – Candle Box Belly Band</title>
<link href="https://fonts.googleapis.com/css2?family=Federant&family=Montserrat:wght@400;500&display=swap" rel="stylesheet">
<style>
  :root {
    --backdrop: #efefef;
    --box-black: #161616;
    --band-white: #ffffff;
    --ink: #151515;
    --rule: #2a2a2a;
  }
  * { box-sizing: border-box; margin: 0; padding: 0; }
  html, body {
    width: 1200px;
    height: 960px;
    overflow: hidden;
    background: var(--backdrop);
  }
  .canvas {
    position: relative;
    width: 1200px;
    height: 960px;
    display: flex;
    align-items: center;
    justify-content: center;
  }
  .box-front {
    position: relative;
    width: 640px;
    height: 640px;
    background: var(--box-black);
    display: flex;
    justify-content: center;
  }
  .belly-band {
    width: 260px;
    height: 100%;
    background: var(--band-white);
    color: var(--ink);
    display: flex;
    flex-direction: column;
    align-items: center;
    padding: 110px 22px 0;
  }
  .brand-mark {
    display: flex;
    flex-direction: column;
    align-items: center;
    gap: 22px;
  }
  .brand-dot {
    width: 64px;
    height: 64px;
    border-radius: 50%;
    background: var(--ink);
  }
  .brand-name {
    font-family: "Montserrat", sans-serif;
    font-weight: 500;
    font-size: 40px;
    letter-spacing: 0.5px;
    white-space: nowrap;
  }
  .fragrance-name {
    margin-top: 88px;
    font-family: "Federant", serif;
    font-size: 29px;
    line-height: 38px;
    text-align: center;
  }
  .product-details {
    margin-top: 18px;
    width: 228px;
    list-style: none;
    font-family: "Montserrat", sans-serif;
    font-size: 13px;
    text-align: center;
    text-transform: uppercase;
  }
  .product-details li {
    padding: 8px 0 7px;
    border-top: 1.5px solid var(--rule);
  }
  .product-details li:last-child {
    border-top: 1.5px solid var(--rule);
  }
</style>
</head>
<body>
  <main class="canvas">
    <section class="box-front" aria-label="Candle box front with belly band">
      <div class="belly-band">
        <div class="brand-mark">
          <span class="brand-dot" aria-hidden="true"></span>
          <span class="brand-name">Hazel &amp; Pip</span>
        </div>
        <h1 class="fragrance-name">Lime, Coconut<br>&amp; Elderfllower</h1>
        <ul class="product-details">
          <li>Hand Poured Soy Candle</li>
          <li>300grams | 50 Hour Burn Time</li>
          <li>Made in Melbourne</li>
        </ul>
      </div>
    </section>
  </main>
</body>
</html>
```